Book Cover Design for a Novella

This book is a whimsical book about random philosophical thoughts. The size of the book is 4X6 inches, about 140 pages long. I would like the background color to be maroon. The title of the book is The Lantern Keeper's Crooked Almanac of Days, and the author name is Delia Marwood. I would like the lettering to either be black or gold, in a font that looks like handwriting. From the lower left corner of the front cover, I would like there to be a gold-colored gardenia.
On the back cover, this is the book summary/description: “We are meant to share our hearts, not give them away. Vulnerability is not the act of placing your heart in someone else’s hands, saying, ‘Keep this safe for me.’ Vulnerability is wearing your heart on your sleeve, showing others your beauty, truths, and fears, and trusting that they will respect you.”
For the author's bio: Delia Marwood is a native of Boulder, Colorado. She enjoys spending time with her cats, eating pasta, and contemplating random things, such as banana spiders, sewage systems, and other huge things that scare her.
I would like all the writing on the back to be in a black, regular font.
I will upload the author's photo, which I would like to be put next to the bio, and I will also attach a rough sketch of what I'd like the cover to look like. Message me with any questions! Thanks.

```html
<!DOCTYPE html>
<html lang="en">
<head>
<meta charset="utf-8">
<title>The Lantern Keeper's Crooked Almanac of Days — Cover</title>
<link rel="stylesheet" href="https://fonts.googleapis.com/css2?family=Great+Vibes&family=Pinyon+Script&display=swap">
<style>
  :root {
    --maroon-deep: #3f0000;
    --maroon: #6a0303;
    --maroon-bright: #7e0606;
    --spine-dark: #2e0000;
    --gold-light: #ffe39a;
    --gold: #e0a93c;
    --gold-dark: #9c6a12;
    --ink: #140000;
    --petal: #f7a52a;
    --petal-light: #ffc95a;
    --leaf: #2f5a25;
    --photo-warm: #b88c72;
    --photo-cool: #8f8a86;
  }
  * { margin: 0; padding: 0; box-sizing: border-box; }
  html, body {
    width: 1200px; height: 844px; overflow: hidden;
    background: var(--maroon-deep);
  }
  .cover {
    position: relative; width: 1200px; height: 844px; overflow: hidden;
  }
  .back-cover {
    position: absolute; left: 0; top: 0; width: 562px; height: 844px;
    background: radial-gradient(ellipse 80% 70% at 45% 40%, var(--maroon-bright), var(--maroon) 55%, var(--maroon-deep) 100%);
  }
  .spine {
    position: absolute; left: 562px; top: 0; width: 75px; height: 844px;
    background: linear-gradient(90deg, var(--spine-dark), var(--maroon) 30%, var(--maroon) 70%, var(--spine-dark));
    display: flex; flex-direction: column; align-items: center;
  }
  .front-cover {
    position: absolute; left: 637px; top: 0; width: 563px; height: 844px;
    background: radial-gradient(ellipse 85% 75% at 55% 35%, var(--maroon-bright), var(--maroon) 55%, var(--maroon-deep) 100%);
  }
  .gold-script {
    font-family: "Great Vibes", cursive;
    color: var(--gold);
    background: linear-gradient(180deg, var(--gold-light) 10%, var(--gold) 55%, var(--gold-dark) 100%);
    -webkit-background-clip: text; background-clip: text;
    -webkit-text-fill-color: transparent;
    filter: drop-shadow(2px 3px 2px rgba(20,0,0,0.7));
  }
  .back-text {
    font-family: "Pinyon Script", cursive;
    font-weight: 400;
    color: var(--ink);
    text-shadow: 0 0 6px rgba(255,60,40,0.25);
    white-space: nowrap;
  }
  .back-text span { display: block; }
  .summary {
    position: absolute; left: 40px; top: 84px; width: 480px;
    font-size: 24px; line-height: 27px; text-align: center;
  }
  .bio-heading {
    position: absolute; right: 56px; top: 414px;
    font-size: 24px; line-height: 27px;
  }
  .bio {
    position: absolute; right: 56px; top: 468px;
    font-size: 24px; line-height: 27px; text-align: right;
  }
  .author-photo {
    position: absolute; left: 41px; top: 537px; width: 207px; height: 267px;
    background: linear-gradient(160deg, var(--photo-cool), var(--photo-warm) 55%, #2a1a16 100%);
  }
  .spine-title, .spine-author {
    writing-mode: vertical-rl;
    font-size: 23px; white-space: nowrap;
  }
  .spine-title { margin-top: 42px; }
  .spine-author { margin-top: auto; margin-bottom: 36px; }
  .front-title {
    position: absolute; left: 0; top: 84px; width: 563px;
    text-align: center; font-size: 50px; line-height: 64px; font-weight: 400;
  }
  .front-title span { display: block; }
  .gardenia {
    position: absolute; left: 47px; top: 469px; width: 432px; height: 375px;
  }
  .front-author {
    position: absolute; right: 24px; top: 764px;
    font-size: 44px; padding-right: 6px;
  }
</style>
</head>
<body>
<main class="cover">
  <section class="back-cover">
    <p class="summary back-text">
      <span>“We are meant to share our hearts, not give them away.</span>
      <span>Vulnerability is not the act of placing your heart in</span>
      <span>someone else’s hands, saying, ‘Keep this safe for me.’</span>
      <span>Vulnerability is wearing your heart on your sleeve,</span>
      <span>showing others your beauty, truths, and fears, and</span>
      <span>trusting that they will respect you.”</span>
    </p>
    <h2 class="bio-heading back-text">Author's Bio:</h2>
    <p class="bio back-text">
      <span>Delia Marwood is a native of Boulder,</span>
      <span>Colorado. She enjoys spending</span>
      <span>time with her cats, eating</span>
      <span>pasta, and contemplating</span>
      <span>random things, such as</span>
      <span>banana spiders, sewage</span>
      <span>systems, and other huge</span>
      <span>things that scare her.</span>
    </p>
    <div class="author-photo" role="img" aria-label="Author portrait photograph"></div>
  </section>

  <section class="spine">
    <span class="spine-title gold-script">The Lantern Keeper's Crooked Almanac of Days</span>
    <span class="spine-author gold-script">Delia Marwood</span>
  </section>

  <section class="front-cover">
    <h1 class="front-title gold-script">
      <span>The Lantern Keeper's</span>
      <span>Crooked Almanac</span>
      <span>of Days</span>
    </h1>
    <svg class="gardenia" viewBox="0 0 432 375" role="img" aria-label="Golden gardenia bloom with green leaves">
      <defs>
        <radialGradient id="bloom-tone" cx="45%" cy="35%" r="60%">
          <stop offset="0" stop-color="var(--petal-light)"/>
          <stop offset="0.6" stop-color="var(--petal)"/>
          <stop offset="1" stop-color="var(--leaf)" stop-opacity="0"/>
        </radialGradient>
      </defs>
      <rect width="432" height="375" fill="url(#bloom-tone)"/>
    </svg>
    <p class="front-author gold-script">Delia Marwood</p>
  </section>
</main>
</body>
</html>
```